Harbourline Plumbing business card full re design & logo design

Harbourline Plumbing is a Sydney based mechanical plumbing contractor company.
We would like a full redesign with new logo etc which we can take to a future website, uniforms, vehicle sign writing etc.
Blue is my preferred choice of colour but i would be open to see a couple of alternatives thrown in the mix to see how they compare. I am open to see on white cards, black cards etc. Open to many new ideas.
Please see attached original business cards which have been used for the last 5 years.

Target Market(s)

Mechanical services industry.

Industry/Entity Type

Plumbing

Contact Information for Business Card

Colin Ashdale
Director

Mob: 0427 590 614
Email: colin@harbourlineplumbing.net.au
PO BOX 816
Merrowdale NSW 2159
Lic: 583106k

Logo Text

Harbourline Plumbing

Font styles to use
Sans Serif

Colors
0655a3
3276b5
0792cd
33a6d7
85cae6
000000
333333
474747

Requirements
Must have
• Things that make it very professional and very well presented.
Nice to have
• Same description or very similar to attached uploaded file
Should not have
• Anything that makes it look unprofessional or cartoony.

```html
<!DOCTYPE html>
<html lang="en">
<head>
<meta charset="utf-8">
<title>Harbourline Plumbing – Business Card</title>
<link rel="stylesheet" href="https://fonts.googleapis.com/css2?family=Arimo:wght@400;700&family=Source+Sans+3:wght@400;600&display=swap">
<style>
  :root {
    --stage: #0d0d0d;
    --band-top: #5a5a5a;
    --band-bottom: #333333;
    --card-white: #fafafa;
    --text-grey: #5e5e5e;
    --brand-blue: #0792cd;
    --sky-blue: #33a6d7;
    --back-top: #00aeef;
    --back-bottom: #203f94;
    --white: #ffffff;
  }
  * { margin: 0; padding: 0; box-sizing: border-box; }
  html, body { width: 999px; height: 1200px; overflow: hidden; background: var(--stage); }
  .canvas { position: relative; width: 999px; height: 1200px; font-family: "Arimo", Arial, sans-serif; }

  /* Front of card (children positioned relative to the card) */
  .card-front { position: absolute; left: 40px; top: 63px; width: 937px; height: 470px; background: var(--card-white); overflow: hidden; }
  .front-band { position: absolute; left: 40px; top: 533px; width: 937px; height: 66px;
    background: linear-gradient(to bottom, var(--band-top), var(--band-bottom)); }
  .brand { position: absolute; left: 42px; top: 199px; display: flex; align-items: center; gap: 14px; }
  .brand-dot { width: 104px; height: 104px; border-radius: 50%; background: var(--brand-blue); }
  .brand-name { font-weight: 700; font-size: 34px; line-height: 1.15; color: var(--brand-blue); }
  .divider { position: absolute; left: 467px; top: 122px; width: 2px; height: 273px;
    background: linear-gradient(to bottom, transparent, var(--sky-blue) 20%, var(--sky-blue) 80%, transparent); }
  .person-name { position: absolute; left: 506px; top: 55px; font-family: "Source Sans 3", sans-serif;
    font-weight: 600; font-size: 41px; line-height: 1.2; color: var(--sky-blue); }
  .person-role { position: absolute; left: 506px; top: 108px; font-family: "Source Sans 3", sans-serif;
    font-size: 23px; line-height: 1.2; color: var(--text-grey); }
  .contact { position: absolute; left: 551px; font-size: 24px; line-height: 31px; color: var(--text-grey); white-space: nowrap; }
  .contact--address { top: 166px; }
  .contact--phone { top: 302px; }
  .contact--email { top: 342px; font-size: 23px; }
  .contact--licence { top: 382px; left: 554px; }
  .icon { position: absolute; }
  .web-ribbon { position: absolute; left: 270px; top: 509px; width: 476px; height: 57px; }
  .web-address { position: absolute; left: 270px; top: 522px; width: 476px; text-align: center;
    font-size: 24px; color: var(--white); }

  /* Back of card */
  .card-back { position: absolute; left: 40px; top: 630px; width: 937px; height: 535px;
    background: linear-gradient(to bottom, var(--back-top), #0085c8 50%, var(--back-bottom)); color: var(--white); }
  .services-title { position: absolute; left: 0; top: 38px; width: 937px; text-align: center;
    font-weight: 700; font-size: 52px; }
  .brand-mark-faint { position: absolute; left: 86px; top: 130px; width: 262px; height: 262px;
    border-radius: 50%; background: rgba(133, 202, 230, 0.45); }
  .tagline { position: absolute; left: 52px; top: 455px; font-weight: 700; font-size: 31px; }
  .specialties-title { position: absolute; left: 585px; top: 172px; font-weight: 700; font-size: 38px; }
  .specialties { position: absolute; left: 585px; top: 226px; list-style: none; }
  .specialties li { position: relative; padding-left: 61px; height: 45.5px; font-size: 29.5px; line-height: 38px; }
  .specialties svg { position: absolute; left: 4px; top: 11px; }
</style>
</head>
<body>
<div class="canvas">

  <section class="card-front">
    <div class="brand">
      <div class="brand-dot"></div>
      <div class="brand-name">Harbourline<br>Plumbing</div>
    </div>
    <div class="divider"></div>
    <div class="person-name">Colin Ashdale</div>
    <div class="person-role">Director</div>

    <svg class="icon" style="left:508px;top:180px" width="26" height="40" viewBox="0 0 26 40" aria-hidden="true">
      <path d="M13 1C6.4 1 1 6.3 1 12.9 1 22 13 39 13 39S25 22 25 12.9C25 6.3 19.6 1 13 1z" fill="var(--sky-blue)"/>
      <circle cx="13" cy="13" r="5" fill="var(--white)"/>
    </svg>
    <div class="contact contact--address">PO BOX 816<br>Merrowdale NSW 2159</div>

    <svg class="icon" style="left:513px;top:307px" width="20" height="26" viewBox="0 0 20 26" aria-hidden="true">
      <rect x="1" y="1" width="18" height="24" rx="3" fill="var(--sky-blue)"/>
      <rect x="5" y="5" width="10" height="14" fill="var(--white)"/>
    </svg>
    <div class="contact contact--phone">0427 590 614</div>

    <svg class="icon" style="left:510px;top:344px" width="26" height="24" viewBox="0 0 26 24" aria-hidden="true">
      <path d="M1 9 13 1l12 8v14H1z" fill="var(--sky-blue)"/>
      <path d="M1 9l12 8 12-8" fill="none" stroke="var(--white)" stroke-width="2"/>
    </svg>
    <div class="contact contact--email">colin@harbourlineplumbing.net.au</div>
    <div class="contact contact--licence">Lic: 583106k</div>
  </section>

  <div class="front-band"></div>
  <svg class="web-ribbon" viewBox="0 0 476 57" aria-hidden="true">
    <polygon points="0,0 8,0 8,24" fill="#1a1a1a"/>
    <polygon points="468,0 476,0 468,24" fill="#1a1a1a"/>
    <polygon points="0,0 476,0 445,57 31,57" fill="var(--sky-blue)"/>
  </svg>
  <div class="web-address">www.harbourlineplumbing.net.au</div>

  <section class="card-back">
    <h1 class="services-title">Mechanical Plumbing Services</h1>
    <div class="brand-mark-faint"></div>
    <p class="tagline">Harbourline have the Solution</p>
    <h2 class="specialties-title">Specialising in:</h2>
    <ul class="specialties">
      <li><svg width="18" height="16" viewBox="0 0 18 16" aria-hidden="true"><path d="M0 0l8 8-8 8zM9 0l8 8-8 8z" fill="var(--white)"/></svg>Make Good</li>
      <li><svg width="18" height="16" viewBox="0 0 18 16" aria-hidden="true"><path d="M0 0l8 8-8 8zM9 0l8 8-8 8z" fill="var(--white)"/></svg>Refurbishment</li>
      <li><svg width="18" height="16" viewBox="0 0 18 16" aria-hidden="true"><path d="M0 0l8 8-8 8zM9 0l8 8-8 8z" fill="var(--white)"/></svg>Tenancy Fit Out</li>
      <li><svg width="18" height="16" viewBox="0 0 18 16" aria-hidden="true"><path d="M0 0l8 8-8 8zM9 0l8 8-8 8z" fill="var(--white)"/></svg>Plant Room Works</li>
      <li><svg width="18" height="16" viewBox="0 0 18 16" aria-hidden="true"><path d="M0 0l8 8-8 8zM9 0l8 8-8 8z" fill="var(--white)"/></svg>Shut Downs</li>
      <li><svg width="18" height="16" viewBox="0 0 18 16" aria-hidden="true"><path d="M0 0l8 8-8 8zM9 0l8 8-8 8z" fill="var(--white)"/></svg>Change Overs</li>
    </ul>
  </section>

</div>
</body>
</html>
```